Psychology and personal development service needs an awesome Web Design

Hi, we are Bright, Steady & Kind, a psychology and personal development service located in Melbourne Australia. We already have a website www.brightsteady&kind.org but it is in great need of a makeover! We add to the website regularly with articles and so we need a space to archive these when they come off the main page, and we have products that we would like to sell internationally so we need a shop page that can convert currencies for international sales and calculate postage and handling. We have a Facebook page that we would like to link as well as a newsletter that we would like to archive on the website. We have just had a logo designed through craft huddle and would like to incorporate this into our website. We want something with high visual impact and uncluttered.
We also run workshops and events so need a tab for this.
Thanks for getting on board!

```html
<!DOCTYPE html>
<html lang="en">
<head>
<meta charset="utf-8">
<title>Bright, Steady &amp; Kind</title>
<link rel="stylesheet" href="https://fonts.googleapis.com/css2?family=Libre+Baskerville:ital,wght@0,400;0,700;1,400&display=swap">
<style>
  :root {
    --page-bg: #e8e9ee;
    --panel-bg: #ffffff;
    --nav-teal: #3dbfa0;
    --nav-active: #4fa88e;
    --tab-teal: #56b697;
    --tab-active: #4fa88e;
    --purple: #7b5aa6;
    --pink: #d9569a;
    --button-blue: #44a7dd;
    --text: #222222;
    --muted: #777777;
    --cover-dark: #2a1e17;
    --cover-mid: #6e5340;
  }
  * { box-sizing: border-box; margin: 0; padding: 0; }
  html, body { width: 705px; height: 1200px; overflow: hidden; }
  body {
    background: var(--page-bg);
    font-family: "Libre Baskerville", Georgia, serif;
    color: var(--text);
    position: relative;
  }
  .site { position: absolute; left: 71px; top: 0; width: 564px; }

  .brand {
    height: 212px;
    display: flex;
    align-items: center;
    justify-content: center;
    gap: 14px;
    padding-bottom: 12px;
  }
  .brand-dot { width: 34px; height: 34px; border-radius: 50%; background: var(--purple); }
  .brand-name { font-size: 30px; color: var(--purple); font-weight: 400; }

  .main-nav { display: flex; height: 47px; background: var(--nav-teal); }
  .main-nav a {
    flex: 1;
    display: flex; align-items: center; justify-content: center;
    color: #fff; text-decoration: none; font-size: 17px;
  }
  .main-nav a.is-active { background: var(--nav-active); flex: 0 0 97px; }

  .panel { background: var(--panel-bg); position: absolute; left: 0; width: 564px; }
  .panel-title { color: var(--purple); font-weight: 700; font-size: 16px; text-align: center; }
  .panel-text { font-size: 12.2px; line-height: 1.6; text-align: center; }

  .welcome { top: 280px; height: 156px; padding: 29px 46px 0; }
  .welcome .panel-title { margin-bottom: 20px; }

  .article { top: 459px; height: 193px; padding: 26px 36px 0; }
  .article-date { font-size: 7.5px; font-style: italic; color: var(--muted); text-align: center; margin: 4px 0 9px; }

  .book { top: 673px; height: 212px; }
  .book-cover {
    position: absolute; left: 11px; top: 12px; width: 126px; height: 190px;
    background: linear-gradient(170deg, var(--cover-mid), var(--cover-dark) 75%);
  }
  .book-info { position: absolute; left: 153px; top: 15px; width: 400px; }
  .book-kicker { color: var(--pink); font-size: 11.5px; }
  .book-title { font-size: 16px; font-weight: 400; margin: 17px 0 7px; }
  .book-blurb { font-size: 9px; line-height: 1.55; }
  .book-actions { position: absolute; right: 10px; bottom: 12px; display: flex; gap: 9px; }
  .button {
    display: flex; align-items: center; justify-content: center;
    height: 41px; background: var(--button-blue); color: #fff;
    font-weight: 700; font-size: 12.5px; text-decoration: none; text-transform: uppercase;
  }
  .button-read { width: 127px; }
  .button-shop { width: 132px; }

  .topics { top: 908px; height: 228px; padding-top: 28px; }
  .topic-tabs { display: flex; gap: 5px; margin: 37px 0 0 26px; }
  .topic-tab {
    height: 28px; padding: 0 11px; background: var(--tab-teal); color: #fff;
    font-size: 12px; display: flex; align-items: center; position: relative;
  }
  .topic-tab.is-open { background: var(--tab-active); }
  .topic-menu {
    position: absolute; left: 110px; top: 110px; width: 143px; height: 83px;
    background: var(--tab-active); padding: 8px 10px; list-style: none;
  }
  .topic-menu::before {
    content: ""; position: absolute; left: 10px; top: -6px;
    border: 6px solid transparent; border-top: 0; border-bottom-color: var(--tab-active);
  }
  .topic-menu li { color: #fff; font-size: 9px; line-height: 18px; }

  .site-footer { position: absolute; top: 1160px; left: 0; font-size: 8.5px; color: var(--muted); }
</style>
</head>
<body>
<div class="site">
  <header class="brand">
    <span class="brand-dot"></span>
    <span class="brand-name">Bright, Steady &amp; Kind</span>
  </header>

  <nav class="main-nav">
    <a href="#" class="is-active">Home</a>
    <a href="#">Shop</a>
    <a href="#">Workshops</a>
    <a href="#">About</a>
    <a href="#">Contact</a>
  </nav>

  <section class="panel welcome">
    <h2 class="panel-title">Hello and welcome!</h2>
    <p class="panel-text">We are a psychology and personal development service located in Melbourne Australia. Phasellus vel velit tincidunt, tempor leo a, ornare turpis. Nullam non lorem massa. Phasellus at metus et orci gravida eleifend.</p>
  </section>

  <section class="panel article">
    <h2 class="panel-title">Article of the month</h2>
    <p class="article-date">October 2014</p>
    <p class="panel-text">We are told that our thoughts have power and that what we think about we bring about, but the truth is that it is the emotional state of mind that determines the outcome not the specific thought. When you are over run with stress or fear or worry or anxiety or any other name for the difficult feelings that you experience, then your request is held back.</p>
  </section>

  <section class="panel book">
    <div class="book-cover" role="img" aria-label="Book cover of Wren: A Daughter's Long Winter by Hanna Verlow"></div>
    <div class="book-info">
      <p class="book-kicker">New book in the shop!</p>
      <h3 class="book-title">Wren: A Daughter's Long Winter</h3>
      <p class="book-blurb">Seventeen-year-old Wren is on a search for identity and transformation as she attempts to come to terms with the death of her mother: a nun—her hero—and light of her life. Wren, who has already lived a challenging existence, is anxious to make sense of her life.</p>
    </div>
    <div class="book-actions">
      <a href="#" class="button button-read">Read more</a>
      <a href="#" class="button button-shop">View in shop</a>
    </div>
  </section>

  <section class="panel topics">
    <h2 class="panel-title">Lets talk about...</h2>
    <div class="topic-tabs">
      <span class="topic-tab">Simplicity</span>
      <span class="topic-tab is-open">Sensitivty</span>
      <span class="topic-tab">Success</span>
      <span class="topic-tab">Parents &amp; children</span>
      <span class="topic-tab">Personality Realms</span>
    </div>
    <ul class="topic-menu">
      <li>This is a article title</li>
      <li>This is a article title</li>
      <li>This is a article title</li>
      <li>This is a article title</li>
    </ul>
  </section>

  <footer class="site-footer">Copyright 2014 © Bright, Steady &amp; Kind</footer>
</div>
</body>
</html>
```